Webdesign - brightparcelhub.com.au - Minimalist

I need someone to make a website for me - I opened an account on brightparcelhub.com.au, paid hundreds and I don't know how to make a webstore.
Someone please help me.

The design is easy.

Minimalist - White background - Black writing.

Font - Brush strokes. Not too fat.

Pages: Home - Shop - Check Out - Contact Us

Let me know if you need more info.
Updates

Target Market(s)

Females aged between 18 ~ 38

Industry/Entity Type

Shop

Font styles to use
Other font styles liked:
• Custom Brush Stroke

Requirements
Must have
• Must be minimalist white background with black writing.

Font must be something of Brush Strokes, I will leave the specific design up to the artists.

```html
<!DOCTYPE html>
<html lang="en">
<head>
<meta charset="utf-8">
<title>Lirela Online</title>
<link rel="stylesheet" href="https://fonts.googleapis.com/css2?family=Open+Sans:wght@400;600;700&family=Oswald:wght@500&family=Kaushan+Script&display=swap">
<style>
:root{
  --ink:#333;
  --ink-soft:#666;
  --muted:#999;
  --line:#e4e4e4;
  --dark:#2b2b2b;
  --panel:#f7f7f7;
  --accent:#f04a4f;
  --orange:#f3a21b;
  --white:#fff;
}
*{box-sizing:border-box;margin:0;padding:0}
html,body{width:727px;height:1200px;overflow:hidden;background:var(--white);font-family:"Open Sans",Arial,sans-serif;color:var(--ink)}
.page{position:relative;width:727px;height:1200px}
.abs{position:absolute}

.topbar{left:0;top:0;width:727px;height:22px;background:var(--dark);color:var(--white);font-size:7.5px}
.topbar .link{position:absolute;top:0;height:22px;line-height:22px;padding-left:14px;border-right:1px solid #444}
.topbar .link svg{position:absolute;left:2px;top:7px}
.topbar .welcome{position:absolute;right:104px;top:0;line-height:22px}
.topbar .welcome span{color:var(--orange)}

.header{left:0;top:22px;width:727px;height:55px;border-bottom:1px solid var(--line)}
.logo{position:absolute;left:104px;top:15px;font-family:"Kaushan Script",cursive;font-size:21px;color:#222}
.contact{position:absolute;left:541px;top:16px;font-size:8px;color:var(--ink-soft);line-height:14px}
.contact-icon{position:absolute;left:505px;top:18px}

.nav{left:0;top:77px;width:727px;height:36px;font-size:9.5px;color:var(--ink)}
.nav a{position:absolute;top:13px;color:inherit;text-decoration:none}
.cart{position:absolute;left:426px;top:9px;width:106px;height:18px;border:1px solid #ddd;font-size:7.5px;line-height:16px;padding-left:20px;color:var(--muted)}
.cart b{color:var(--accent);font-weight:400}
.cart .total{position:absolute;right:6px;top:0;color:var(--ink);font-size:8px}
.search{position:absolute;left:543px;top:9px;width:81px;height:18px;border:1px solid #ddd;font-size:7px;line-height:16px;padding-left:7px;color:var(--muted)}

.hero{left:0;top:113px;width:727px;height:329px;background:linear-gradient(90deg,#7d8a96 0%,#a3aeb8 35%,#c9c4c0 55%,#8e99a4 100%)}
.arrow{position:absolute;top:152px;width:29px;height:29px;border-radius:50%;background:rgba(90,90,90,.75)}
.badge{position:absolute;border-radius:50%;background:var(--white);text-align:center}
.badge .small{font-size:10px;color:var(--ink-soft)}
.badge .big{font-family:"Oswald",sans-serif;color:var(--accent)}
.sale{position:absolute;left:288px;top:153px;width:157px;height:157px;border-radius:50%;background:rgba(55,55,55,.92);color:var(--white);text-align:center}
.sale .title{font-family:"Oswald",sans-serif;font-size:38px;line-height:42px;margin-top:27px}
.sale .sub{font-size:12px;margin-top:4px}

.promo{top:463px;width:254px;height:114px;color:var(--white)}
.promo h3{position:absolute;left:14px;top:18px;font-family:"Kaushan Script",cursive;font-weight:400;font-size:19px}
.promo p{position:absolute;left:16px;top:47px;font-size:12px;letter-spacing:.3px}
.promo .btn{position:absolute;left:14px;top:70px;background:#222;font-size:10px;padding:3px 8px}

.section-title{left:104px;top:598px;font-size:13px;letter-spacing:.5px;color:var(--ink)}
.pager{top:598px;width:12px;height:12px;border:1px solid #ccc;border-radius:50%}

.card{width:121px;height:153px;border:1px solid var(--line);border-radius:3px;box-shadow:0 2px 2px rgba(0,0,0,.05);background:var(--white)}
.card .img{position:absolute;left:20px;top:8px;width:80px;height:76px;background:radial-gradient(circle,#e6ddd0 0%,#fff 72%)}
.card .desc{position:absolute;left:10px;top:90px;font-size:8px;color:var(--ink-soft)}
.card .rule{position:absolute;left:0;top:108px;width:119px;border-top:1px solid var(--line)}
.card .add{position:absolute;left:10px;top:121px;width:49px;height:18px;background:#333;color:var(--white);border-radius:3px;font-size:6.5px;line-height:18px;text-align:center}
.card .price{position:absolute;left:71px;top:123px;font-size:9.5px;color:var(--ink-soft)}

.feature{top:980px;width:164px;height:86px;background:var(--panel);border:1px solid var(--line);border-radius:3px}
.feature h4{position:absolute;left:64px;top:12px;font-size:9px;font-weight:400;color:var(--ink)}
.feature p{position:absolute;left:64px;top:29px;width:92px;font-size:6px;line-height:10.5px;color:var(--ink-soft)}
.feature .more{position:absolute;left:64px;top:66px;font-size:6px;font-weight:600}
.feature svg{position:absolute;left:12px;top:24px}

.finder{left:104px;top:1087px;width:520px;height:52px;background:var(--panel);border:1px solid var(--line);border-radius:3px}
.finder .field{position:absolute;left:15px;top:12px;width:385px;height:27px;background:var(--white);border-radius:3px;font-size:8.5px;color:var(--muted);line-height:27px;padding-left:10px}
.finder .go{position:absolute;left:407px;top:10px;width:96px;height:30px;background:var(--accent);border-radius:3px;color:var(--white);font-size:9.5px;line-height:30px;text-align:center}

.footer{left:0;top:1160px;width:727px;border-top:1px solid var(--line);height:40px;font-size:6.5px;color:var(--ink-soft)}
.footer .copy{position:absolute;left:104px;top:18px}
.footer .dot{position:absolute;top:12px;width:15px;height:15px;border-radius:50%}
.footer .legal{position:absolute;left:522px;top:18px}
.footer .code{position:absolute;left:670px;top:18px}
</style>
</head>
<body>
<div class="page">

  <div class="abs topbar">
    <div class="link" style="left:104px;width:65px"><svg width="8" height="7"><rect x="0" y="1" width="8" height="6" rx="1" fill="#fff"/></svg>My account</div>
    <div class="link" style="left:180px;width:70px"><svg width="8" height="7"><rect x="0" y="1" width="8" height="6" rx="1" fill="#fff"/></svg>My wishlist</div>
    <div class="link" style="left:250px;width:55px;border:none"><svg width="8" height="7"><path d="M0 1h2l1 4h4l1-3H3" fill="none" stroke="#fff"/></svg>Checkout</div>
    <div class="welcome">Welcome visitor you can <span>Login</span> or <span>Create an account</span></div>
  </div>

  <header class="abs header">
    <div class="logo">Lirela Online</div>
    <svg class="contact-icon" width="20" height="22" viewBox="0 0 20 22"><path d="M4 1c-3 2-3 8 2 14s10 7 12 5l-3-4-3 1c-2-1-5-5-5-7l2-2z" fill="#bbb"/></svg>
    <div class="contact">info@lirelaonline.com<br>+(19) 555 014 208</div>
  </header>

  <nav class="abs nav">
    <a style="left:103px">Home</a>
    <a style="left:147px">About us</a>
    <a style="left:202px">Shop</a>
    <a style="left:242px">Checkout</a>
    <a style="left:299px">Contact us</a>
    <div class="cart">
      <svg style="position:absolute;left:5px;top:4px" width="10" height="8"><path d="M0 1h2l1 5h6l1-4H3" fill="none" stroke="#666"/></svg>
      Cart <b>0</b> items<span class="total">47,99 $</span>
    </div>
    <div class="search">Search...
      <svg style="position:absolute;right:5px;top:5px" width="8" height="8"><circle cx="3" cy="3" r="2.4" fill="none" stroke="#aaa"/><path d="M5 5l3 3" stroke="#aaa"/></svg>
    </div>
  </nav>

  <section class="abs hero" role="img" aria-label="Photo of a smiling woman with long dark hair holding colourful beaded necklaces against a grey wall">
    <div class="arrow" style="left:42px"><svg width="29" height="29"><path d="M17 9l-5 5.5 5 5.5" fill="none" stroke="#fff" stroke-width="2"/></svg></div>
    <div class="arrow" style="left:677px"><svg width="29" height="29"><path d="M12 9l5 5.5-5 5.5" fill="none" stroke="#fff" stroke-width="2"/></svg></div>
    <div class="badge" style="left:124px;top:153px;width:75px;height:75px">
      <div class="small" style="margin-top:18px">Delivery</div>
      <div class="big" style="font-size:24px;line-height:24px">Free</div>
    </div>
    <div class="sale">
      <div class="title">Great<br>Sale</div>
      <div class="sub">On all models</div>
    </div>
    <div class="badge" style="left:534px;top:153px;width:75px;height:75px">
      <div class="small" style="margin-top:18px">Starting from</div>
      <div class="big" style="font-size:27px;line-height:28px">429 <span style="font-size:13px">$</span></div>
    </div>
  </section>

  <div class="abs promo" style="left:105px;background:linear-gradient(90deg,#5e6770,#8d949a 55%,#b7b9bb)" role="img" aria-label="Photo of black high heel shoes on paving stones">
    <h3>New Season...</h3>
    <p>Shoes &amp; Dresses</p>
    <div class="btn">Shop Now</div>
  </div>
  <div class="abs promo" style="left:371px;background:linear-gradient(90deg,#6a6b6c,#7c7d7e 60%,#4a4a4a)" role="img" aria-label="Photo of a blonde woman wearing earrings against a grey backdrop">
    <h3>Womens</h3>
    <p>Necklaces</p>
    <div class="btn">Shop Now</div>
  </div>

  <h2 class="abs section-title" style="font-weight:400">NEW ARRIVALS</h2>
  <div class="abs pager" style="left:597px"><svg width="10" height="10"><path d="M6 3l-2 2 2 2" fill="none" stroke="#666"/></svg></div>
  <div class="abs pager" style="left:612px"><svg width="10" height="10"><path d="M4 3l2 2-2 2" fill="none" stroke="#666"/></svg></div>

  <div class="abs card" style="left:104px;top:628px"><div class="img" role="img" aria-label="Silver heart pendant necklace"></div><div class="desc">Adipiscing elit, sed diam...</div><div class="rule"></div><div class="add">Add to cart</div><div class="price">$225.25</div></div>
  <div class="abs card" style="left:238px;top:628px"><div class="img" role="img" aria-label="Gold and crystal drop necklace"></div><div class="desc">Adipiscing elit, sed diam...</div><div class="rule"></div><div class="add">Add to cart</div><div class="price">$225.25</div></div>
  <div class="abs card" style="left:370px;top:628px"><div class="img" role="img" aria-label="Multicoloured beaded bib necklace"></div><div class="desc">Adipiscing elit, sed diam...</div><div class="rule"></div><div class="add">Add to cart</div><div class="price">$225.25</div></div>
  <div class="abs card" style="left:503px;top:628px"><div class="img" role="img" aria-label="Chain necklace with flower stones"></div><div class="desc">Adipiscing elit, sed diam...</div><div class="rule"></div><div class="add">Add to cart</div><div class="price">$225.25</div></div>

  <div class="abs card" style="left:104px;top:799px"><div class="img" role="img" aria-label="Gold necklace with coloured gems"></div><div class="desc">Adipiscing elit, sed diam...</div><div class="rule"></div><div class="add">Add to cart</div><div class="price">$225.25</div></div>
  <div class="abs card" style="left:238px;top:799px"><div class="img" role="img" aria-label="Gold statement necklace with orange stones"></div><div class="desc">Adipiscing elit, sed diam...</div><div class="rule"></div><div class="add">Add to cart</div><div class="price">$225.25</div></div>
  <div class="abs card" style="left:370px;top:799px"><div class="img" role="img" aria-label="Layered gold coin necklace"></div><div class="desc">Adipiscing elit, sed diam...</div><div class="rule"></div><div class="add">Add to cart</div><div class="price">$225.25</div></div>
  <div class="abs card" style="left:503px;top:799px"><div class="img" role="img" aria-label="Gold double heart pendant"></div><div class="desc">Adipiscing elit, sed diam...</div><div class="rule"></div><div class="add">Add to cart</div><div class="price">$225.25</div></div>

  <div class="abs feature" style="left:104px">
    <svg width="30" height="30"><path d="M2 4h4l5 18" fill="none" stroke="#444" stroke-width="2"/><rect x="12" y="9" width="10" height="8" fill="#444" transform="rotate(-15 17 13)"/><circle cx="12" cy="24" r="3" fill="#444"/></svg>
    <h4>Very fast delivery.</h4>
    <p>Lorem ipsum dolor sit amet, consectetur adipiscing elit. Sed viverra, urna quis dignissim</p>
    <div class="more">MORE →</div>
  </div>
  <div class="abs feature" style="left:282px">
    <svg width="32" height="30"><path d="M16 2l-9 8M16 2l9 8" stroke="#444" fill="none"/><rect x="1" y="10" width="30" height="17" rx="2" fill="#444"/><text x="16" y="23" font-size="10" fill="#fff" text-anchor="middle" font-family="Open Sans,sans-serif">SALE</text></svg>
    <h4>Every week discounts.</h4>
    <p>Lorem ipsum dolor sit amet, consectetur adipiscing elit. Sed viverra, urna quis dignissim</p>
    <div class="more">MORE →</div>
  </div>
  <div class="abs feature" style="left:460px">
    <svg width="30" height="30"><path d="M11 3h8l-2 5c6 3 9 9 7 14s-14 5-17 0 1-11 7-14z" fill="#444"/><text x="15" y="24" font-size="10" fill="#fff" text-anchor="middle" font-family="Open Sans,sans-serif">$</text></svg>
    <h4>Money saver.</h4>
    <p>Lorem ipsum dolor sit amet, consectetur adipiscing elit. Sed viverra, urna quis dignissim</p>
    <div class="more">MORE →</div>
  </div>

  <div class="abs finder">
    <div class="field">Looking for another product? Use this search form and hit enter...</div>
    <div class="go">Search Product</div>
  </div>

  <footer class="abs footer">
    <div class="copy">©2013 - 2014 Lirela Online., All Rights Reserved.</div>
    <div class="dot" style="left:363px;background:#3b5998"></div>
    <div class="dot" style="left:382px;background:#2fa6dd"></div>
    <div class="dot" style="left:401px;background:#c4302b"></div>
    <div class="legal">Terms of Service | Privacy Policy</div>
    <div class="code">C7</div>
  </footer>

</div>
</body>
</html>
```